I need a business card design for a new company that will be doing consulting work around issues of cultural competency, and diversity and inclusion. I would like the design to be crisp and clear with bold but conservative colors and incorporate shades of blue

Target Market(s)

Small businesses, schools, non-profits

Industry/Entity Type

Consulting

Font styles to use
Serif
Sans Serif

Colors
0c5ba6
6b449b
3276b5
0292cd

Requirements
Must have
• A Morrow Venture (name of company)
• Lemlem Tavish
• CEO
• lemlem@amorrowventure.com
• (215)483-2756

```html
<!DOCTYPE html>
<html lang="en">
<head>
<meta charset="utf-8">
<title>A Morrow Venture — Business Card</title>
<link rel="stylesheet" href="https://fonts.googleapis.com/css2?family=Lato:wght@300;400;700&display=swap">
<style>
  :root {
    --backdrop: #1b1e23;
    --card-blue: #1f3e7e;
    --card-blue-light: #24468a;
    --ink-white: #ffffff;
    --ink-soft: #dbe3f2;
    --accent-cyan: #36aee6;
  }
  * { box-sizing: border-box; margin: 0; padding: 0; }
  html, body {
    width: 1200px; height: 900px; overflow: hidden;
    background: var(--backdrop);
    font-family: "Lato", Arial, sans-serif;
  }
  .canvas {
    position: relative; width: 1200px; height: 900px;
    display: flex; align-items: center; justify-content: center;
  }
  .business-card {
    position: relative; width: 1000px; height: 580px;
    border-radius: 44px;
    background: linear-gradient(160deg, var(--card-blue-light), var(--card-blue));
    color: var(--ink-white);
  }
  .holder { position: absolute; left: 72px; top: 62px; }
  .holder-name { font-size: 46px; font-weight: 700; letter-spacing: -0.5px; }
  .holder-role { font-size: 26px; font-weight: 300; margin-top: 2px; color: var(--ink-soft); }
  .contact-list {
    position: absolute; left: 44px; bottom: 68px;
    list-style: none; display: flex; flex-direction: column; gap: 12px;
  }
  .contact-item { display: flex; align-items: center; gap: 16px; font-size: 24px; font-weight: 400; }
  .contact-icon { width: 26px; height: 26px; flex: none; }
  .contact-domain { color: var(--accent-cyan); }
  .company-name {
    position: absolute; right: 150px; bottom: 96px;
    font-size: 44px; font-weight: 700; line-height: 1.05;
    color: var(--accent-cyan); text-transform: uppercase; text-align: left;
  }
</style>
</head>
<body>
<main class="canvas">
  <article class="business-card">
    <header class="holder">
      <h1 class="holder-name">Lemlem Tavish</h1>
      <p class="holder-role">CEO</p>
    </header>

    <ul class="contact-list">
      <li class="contact-item">
        <svg class="contact-icon" viewBox="0 0 24 24" aria-hidden="true">
          <path fill="#fff" d="M6.6 10.8a15.1 15.1 0 0 0 6.6 6.6l2.2-2.2c.3-.3.7-.4 1-.2 1.1.4 2.3.6 3.6.6.6 0 1 .4 1 1V20c0 .6-.4 1-1 1A17 17 0 0 1 3 4c0-.6.4-1 1-1h3.5c.6 0 1 .4 1 1 0 1.3.2 2.5.6 3.6.1.3 0 .7-.2 1z"/>
        </svg>
        <span>(215)483-2756</span>
      </li>
      <li class="contact-item">
        <svg class="contact-icon" viewBox="0 0 24 24" aria-hidden="true">
          <rect x="2" y="5" width="20" height="14" rx="1" fill="#fff"/>
          <path d="M2.5 5.5 12 13l9.5-7.5M2.5 18.5l7-6.5M21.5 18.5l-7-6.5" fill="none" stroke="var(--card-blue)" stroke-width="1.6"/>
        </svg>
        <span>lemlem@amorrowventure.com</span>
      </li>
      <li class="contact-item">
        <svg class="contact-icon" viewBox="0 0 24 24" aria-hidden="true">
          <g fill="none" stroke="#fff" stroke-width="1.6">
            <circle cx="12" cy="12" r="10"/>
            <ellipse cx="12" cy="12" rx="4.5" ry="10"/>
            <path d="M2 12h20M4 7h16M4 17h16"/>
          </g>
        </svg>
        <span>www.<span class="contact-domain">lemlemmorrowventure.com</span></span>
      </li>
    </ul>

    <p class="company-name">A Morrow<br>Venture</p>
  </article>
</main>
</body>
</html>
```